Catalogue Design Project

We require a new 2013 catalogue cover designed ( front & back with a one inch wide spine) for our business, Brellock Office Supplies. We have been established for 36 years and we supply all sorts of companies across the UK with a Variety of Office Stationery, Computer Products, Print, Furniture, Catering and Cleaning products within the UK - you can browse our catalogue on our website www.brellock.co.uk - using test as both user id and password.
We are serious about customer service; ensure we do the very best for our clients with the best prices. For us it’s all about the image we portray to our clients, we don’t want the cover to look like it’s the cover of a Yacht catalogue, nor do we want it to look like a trashy magazine.
The main priority of this design is that the Catalogue looks professional and appealing. Good use of colour, possibly incorporating elements of what we do would be of advantage.
(Please visit our website www.brellock.co.uk for details).
The Catalogue is to be A4 in size, MUST have our company logo in on the front, which we will supply, but for the start obtainable from our site)
The Catalogue covers will have insides both front and back that we will be printing on. Your design and use of colours should be able to flow onto these pages so as we can print on a continuation of your design.
**UPDATE - Please note the content is already designed, this is for the front/back cover and inside covers**
There will be a few edits after we make a choice...
if you need anything from us then please email us on jpoll@brellock.co.uk
Best of luck
Reason: Deaedline Extended to give you all a chance to get your designs in!!
Reason: Having some great creative ideas in, so herew is a chance for one last push before we make our decision.
PROJECT NOW GUARANTEED.!!
Due to the High Quality of designs being submitted - we are now happy to commit to one of you! Keep the designs coming!
Good Luck!
Target Market(s)
The Buyers of our products are corporate companies
Industry/Entity Type
Printing
Look and feel

```html
<!DOCTYPE html>
<html lang="en">
<head>
<meta charset="utf-8">
<title>Brellock Office Supplies – 2013 Catalogue Cover</title>
<link href="https://fonts.googleapis.com/css2?family=Arimo:ital,wght@0,400;0,700;1,400&display=swap" rel="stylesheet">
<style>
  :root {
    --backdrop: #5b5b5b;
    --cover-yellow: #f4d625;
    --stripe-yellow: #f8e570;
    --pale-yellow: #fbf0a8;
    --band-grey: #ecece8;
    --logo-gold: #d8b61c;
    --white: #ffffff;
    --photo-tone-a: #3a6fb0;
    --photo-tone-b: #e8d84a;
  }
  * { margin: 0; padding: 0; box-sizing: border-box; }
  html, body {
    width: 1200px; height: 1000px; overflow: hidden;
    background: var(--backdrop);
    font-family: "Arimo", Arial, sans-serif;
  }
  .cover-spread {
    position: absolute; left: 50px; top: 134px;
    width: 1100px; height: 731px;
    background: var(--cover-yellow);
    overflow: hidden;
  }
  .spread-art { position: absolute; inset: 0; }
  .back-cover, .spine, .front-cover { position: absolute; top: 0; height: 100%; }
  .back-cover { left: 0; width: 517px; text-align: center; color: var(--white); }
  .spine { left: 517px; width: 66px; }
  .front-cover { left: 583px; width: 517px; color: var(--white); }

  .brand-name { font-weight: 700; letter-spacing: 3px; }
  .brand-sub { font-size: 10px; letter-spacing: 0.5px; }
  .tagline { font-style: italic; font-size: 10px; letter-spacing: 0.4px; }

  .back-cover .brand { position: absolute; top: 240px; width: 100%; }
  .back-cover .brand-name { font-size: 22px; }
  .back-cover .brand-sub { margin-top: 1px; }
  .back-cover .tagline { margin-top: 8px; }

  .year { font-weight: 700; font-size: 72px; line-height: 1; letter-spacing: 2px; }
  .catalogue-word { font-size: 25px; letter-spacing: 1.5px; line-height: 1.1; }
  .web-address { font-weight: 700; font-size: 16px; letter-spacing: 0.8px; }

  .back-cover .title-block { position: absolute; top: 338px; width: 100%; }
  .back-cover .web-address { position: absolute; top: 458px; width: 100%; }

  .front-cover .title-block { position: absolute; left: 57px; top: 228px; }
  .front-cover .web-address { position: absolute; left: 57px; top: 358px; }
  .front-cover .brand {
    position: absolute; right: 40px; top: 612px; text-align: center; color: var(--logo-gold);
  }
  .front-cover .brand-name { font-size: 38px; font-weight: 400; letter-spacing: 5px; }
  .front-cover .brand-sub { text-align: right; margin-top: -2px; font-size: 11px; }
  .front-cover .tagline { display: block; margin-top: 8px; font-size: 11px; font-weight: 700; }

  .spine-title, .spine-brand {
    position: absolute; left: 50%;
    transform: translateX(-50%) rotate(90deg);
    white-space: nowrap; color: var(--white);
  }
  .spine-title { top: 150px; font-weight: 700; font-size: 21px; letter-spacing: 1px; }
  .spine-brand { top: 430px; text-align: left; }
  .spine-brand .brand-name { font-size: 20px; font-weight: 400; }
  .spine-brand .brand-sub { font-size: 9px; text-align: right; }
</style>
</head>
<body>
<main class="cover-spread">
  <svg class="spread-art" width="1100" height="731" viewBox="0 0 1100 731" aria-hidden="true">
    <!-- spine edge lines -->
    <rect x="517" y="0" width="4" height="731" fill="var(--stripe-yellow)"/>
    <rect x="579" y="0" width="4" height="731" fill="var(--stripe-yellow)"/>
    <!-- sweeping bottom bands -->
    <polygon points="0,640 1100,545 1100,731 0,731" fill="var(--stripe-yellow)" opacity="0.8"/>
    <polygon points="0,665 1100,575 1100,731 0,731" fill="var(--pale-yellow)"/>
    <polygon points="0,690 1100,600 1100,731 0,731" fill="var(--band-grey)"/>
  </svg>

  <section class="back-cover">
    <div class="brand">
      <div class="brand-name">BRELLOCK</div>
      <div class="brand-sub">Office Supplies</div>
      <div class="tagline">The reliable supplier that makes your office work.</div>
    </div>
    <div class="title-block">
      <div class="year">2013</div>
      <div class="catalogue-word">Catalogue</div>
    </div>
    <div class="web-address">www.brellock.co.uk</div>
  </section>

  <section class="spine">
    <div class="spine-title">2013 Catalogue</div>
    <div class="spine-brand">
      <div class="brand-name">BRELLOCK</div>
      <div class="brand-sub">Office Supplies</div>
    </div>
  </section>

  <section class="front-cover">
    <div class="title-block">
      <div class="year">2013</div>
      <div class="catalogue-word">Catalogue</div>
    </div>
    <div class="web-address">www.brellock.co.uk</div>

    <svg class="product-wedge" style="position:absolute;left:0;top:0" width="517" height="731" viewBox="0 0 517 731"
         role="img" aria-label="Collage of office supplies: pens, paper clips, sticky notes, tape, discs and a computer mouse">
      <defs>
        <linearGradient id="wedgeTones" x1="0" y1="0" x2="1" y2="1">
          <stop offset="0" stop-color="var(--photo-tone-a)"/>
          <stop offset="0.55" stop-color="#6c8fb8"/>
          <stop offset="1" stop-color="var(--photo-tone-b)"/>
        </linearGradient>
      </defs>
      <polygon points="57,429 517,290 517,731 412,731 374,595" fill="url(#wedgeTones)"/>
    </svg>

    <div class="brand">
      <div class="brand-name">BRELLOCK</div>
      <div class="brand-sub">Office Supplies</div>
      <span class="tagline">The reliable supplier that makes your office work</span>
    </div>
  </section>
</main>
</body>
</html>
```